Velisto Events Business Card

We need a business cards that stands out to our clients. We are company who targets prestige clients to spend money with us on experiences, so our image needs to be prestige
Target Market(s)
Corporate
Contact Information for Business Card
There will be four different names on the business cards
Dana Morrowby
Director
O: 02 5147 3086
M: 0451 692 038
E: info@velistoevents.example.au
Facebook: @velistoevents
Instagram: velistoevents
www.velistoevents.example.au
Nathaniel Morrowby
Director
O: 02 5147 3086
M: 0467 215 904
Facebook: @velistoevents
Instagram: velistoevents
www.velistoevents.example.au
Teodor Vinkel
Director
O: 02 5147 3086
M: 0478 903 527
Facebook: @velistoevents
Instagram: velistoevents
www.velistoevents.example.au
Mabel Hartung
Director
O: 02 5147 3086
Facebook: @velistoevents
Instagram: velistoevents
www.velistoevents.example.au
Colors
Designer to choose colors to be used in the design.
Look and feel

```html
<!DOCTYPE html>
<html lang="en">
<head>
<meta charset="UTF-8">
<title>Velisto Events Business Card</title>
<link rel="stylesheet" href="https://fonts.googleapis.com/css2?family=Cinzel:wght@500&family=Open+Sans:wght@400;600&display=swap">
<style>
  :root {
    --gold: #e3bc4a;
    --gold-light: #ecca58;
    --gold-deep: #d5aa35;
    --navy: #27224f;
    --navy-deep: #1f1a43;
    --muted: #9c8f6a;
    --backdrop: #d9d9d9;
  }
  * { box-sizing: border-box; margin: 0; padding: 0; }
  html, body { width: 1200px; height: 880px; overflow: hidden; }
  body {
    background: var(--backdrop);
    font-family: "Open Sans", Arial, sans-serif;
    position: relative;
  }
  .card {
    position: absolute;
    width: 560px;
    height: 320px;
    overflow: hidden;
    box-shadow: 0 6px 18px rgba(0,0,0,0.18);
  }
  .card--back { left: 70px; top: 90px; }
  .card--front { left: 570px; top: 470px; }
  .card__surface {
    position: absolute; inset: 0;
    background: linear-gradient(135deg, var(--gold-deep), var(--gold) 45%, var(--gold-light));
  }
  .brand {
    position: absolute;
    left: 0; right: 0;
    text-align: center;
    color: var(--navy);
  }
  .brand__mark {
    display: block;
    width: 34px; height: 34px;
    margin: 0 auto 12px;
    border: 3px solid var(--navy);
  }
  .brand__name {
    font-family: "Cinzel", Georgia, serif;
    font-weight: 500;
    font-size: 30px;
    letter-spacing: 9px;
    line-height: 1;
    padding-left: 9px;
  }
  .brand__sub {
    font-family: "Cinzel", Georgia, serif;
    font-weight: 500;
    font-size: 12px;
    letter-spacing: 6px;
    margin-top: 6px;
    padding-left: 6px;
  }
  .card--back .brand { top: 62px; }
  .card--front .brand { top: 30px; }

  .social-band {
    position: absolute;
    left: 0; right: 0; bottom: 0;
    height: 78px;
    background: var(--navy);
    display: flex;
    align-items: center;
    justify-content: center;
    gap: 22px;
    color: var(--gold);
    font-size: 13px;
    font-weight: 600;
  }
  .social-band__dot {
    width: 20px; height: 20px;
    border: 2px solid var(--gold);
    border-radius: 50%;
  }
  .social-band__divider {
    width: 2px; height: 18px;
    background: var(--gold);
  }

  .person-band {
    position: absolute;
    left: 0; right: 0;
    top: 156px;
    height: 72px;
    background: var(--navy);
    text-align: center;
    padding-top: 12px;
  }
  .person-band__name {
    color: var(--gold);
    font-size: 21px;
    line-height: 1.2;
  }
  .person-band__role {
    color: var(--muted);
    font-size: 14px;
  }

  .contacts {
    position: absolute;
    left: 0; right: 0;
    top: 238px;
    display: flex;
    justify-content: center;
    align-items: flex-end;
    gap: 14px;
    color: var(--navy-deep);
    font-size: 12.5px;
    font-weight: 600;
  }
  .contacts__item {
    display: flex;
    flex-direction: column;
    align-items: center;
    gap: 5px;
    line-height: 1.4;
  }
  .contacts__lines {
    display: flex;
    flex-direction: column;
    align-items: center;
  }
  .contacts__icon { width: 15px; height: 15px; fill: var(--navy); }
  .contacts__divider {
    width: 2px; height: 26px;
    background: var(--navy);
    margin-bottom: 2px;
  }
</style>
</head>
<body>

  <section class="card card--back" aria-label="Business card back">
    <div class="card__surface" role="img" aria-label="Gold surface with a faint repeating crest pattern"></div>
    <div class="brand">
      <span class="brand__mark"></span>
      <div class="brand__name">VELISTO</div>
      <div class="brand__sub">EVENTS</div>
    </div>
    <div class="social-band">
      <span>velistoevents</span>
      <span class="social-band__dot"></span>
      <span class="social-band__divider"></span>
      <span class="social-band__dot"></span>
      <span>@velistoevents</span>
    </div>
  </section>

  <section class="card card--front" aria-label="Business card front">
    <div class="card__surface" role="img" aria-label="Gold surface with a faint repeating crest pattern"></div>
    <div class="brand">
      <span class="brand__mark"></span>
      <div class="brand__name">VELISTO</div>
      <div class="brand__sub">EVENTS</div>
    </div>
    <div class="person-band">
      <div class="person-band__name">Dana Morrowby</div>
      <div class="person-band__role">Director</div>
    </div>
    <div class="contacts">
      <div class="contacts__item">
        <svg class="contacts__icon" viewBox="0 0 24 24" aria-hidden="true"><path d="M6.6 10.8a15.1 15.1 0 0 0 6.6 6.6l2.2-2.2a1 1 0 0 1 1-.25 11.4 11.4 0 0 0 3.6.57 1 1 0 0 1 1 1V20a1 1 0 0 1-1 1A17 17 0 0 1 3 4a1 1 0 0 1 1-1h3.5a1 1 0 0 1 1 1c0 1.25.2 2.45.57 3.57a1 1 0 0 1-.25 1z"/></svg>
        <span class="contacts__lines">
          <span>O: 02 5147 3086</span>
          <span>M: 0451 692 038</span>
        </span>
      </div>
      <span class="contacts__divider"></span>
      <div class="contacts__item">
        <svg class="contacts__icon" viewBox="0 0 24 24" aria-hidden="true"><path d="M2 5h20v2l-10 6L2 7z"/><path d="M2 9l10 6 10-6v10H2z"/></svg>
        <span>info@velistoevents.example.au</span>
      </div>
      <span class="contacts__divider"></span>
      <div class="contacts__item">
        <svg class="contacts__icon" viewBox="0 0 24 24" aria-hidden="true"><path d="M12 2a10 10 0 1 0 0 20 10 10 0 0 0 0-20zm6.9 6h-2.9a15.7 15.7 0 0 0-1.4-3.6A8 8 0 0 1 18.9 8zM12 4c.8 1.2 1.5 2.5 1.9 4h-3.8c.4-1.5 1.1-2.8 1.9-4zM4.3 14a8.2 8.2 0 0 1 0-4h3.4a16.5 16.5 0 0 0 0 4zm.8 2h2.9c.3 1.3.8 2.5 1.4 3.6A8 8 0 0 1 5.1 16zM8 8H5.1a8 8 0 0 1 4.3-3.6C8.8 5.5 8.4 6.7 8 8zm4 12c-.8-1.2-1.5-2.5-1.9-4h3.8c-.4 1.5-1.1 2.8-1.9 4zm2.3-6H9.7a14.7 14.7 0 0 1 0-4h4.6a14.7 14.7 0 0 1 0 4zm.3 5.6c.6-1.1 1.1-2.3 1.4-3.6h2.9a8 8 0 0 1-4.3 3.6zm1.7-5.6a16.5 16.5 0 0 0 0-4h3.4a8.2 8.2 0 0 1 0 4z"/></svg>
        <span>www.velistoevents.example.au</span>
      </div>
    </div>
  </section>

</body>
</html>
```